Landing Page for Social Media Optimization

We need a Landing page made for Social Media Optimization we are going to be calling this QuenPeak an entire package that is for small to large businesses. We will manage all aspects of social media from Plinkora, Wendlo Trovaxe, Marbix+ for a monthly fee helping them reach customers.

We simply need a web page that shows "The Package" and with a form that lets the user fill in there contact details so we can get in touch. The contact details we'd like to collect are

Name
Email
Company
Telephone

```html
<!DOCTYPE html>
<html lang="en">
<head>
<meta charset="utf-8">
<title>QuenPeak – Social Media Optimization</title>
<link rel="stylesheet" href="https://fonts.googleapis.com/css2?family=Montserrat:wght@300;400;600;700&display=swap">
<style>
  :root {
    --ink-light: #ffffff;
    --ink-muted: #d9d2c8;
    --panel: rgba(12, 8, 6, 0.68);
    --field: #ffffff;
    --placeholder: #9a9a9a;
    --accent: #9c3a86;
    --accent-dark: #6e2460;
    --ok: #3cb04a;
    --social: #1d4f73;
    --social-dark: #123650;
    --scene-deep: #2a160c;
    --scene-mid: #6b4226;
    --scene-warm: #a87a4e;
    --scene-pale: #d8c4a0;
  }
  * { box-sizing: border-box; margin: 0; padding: 0; }
  html, body { width: 1200px; height: 593px; overflow: hidden; }
  body {
    position: relative;
    font-family: "Montserrat", Arial, sans-serif;
    color: var(--ink-light);
    background: var(--scene-deep);
  }
  .hero-backdrop {
    position: absolute; inset: 0;
    background:
      radial-gradient(ellipse 420px 260px at 900px 300px, rgba(40,30,30,0.85), transparent 70%),
      radial-gradient(ellipse 520px 240px at 330px 500px, rgba(216,196,160,0.75), transparent 70%),
      linear-gradient(180deg, var(--scene-deep) 0%, #3d2213 35%, var(--scene-mid) 62%, var(--scene-warm) 100%);
  }
  .hero-backdrop::after {
    content: ""; position: absolute; inset: 0;
    background: rgba(0,0,0,0.18);
  }
  .brand {
    position: absolute; left: 281px; top: 46px;
    display: flex; align-items: flex-start; gap: 4px;
  }
  .brand-name { font-size: 25px; font-weight: 600; letter-spacing: -0.3px; }
  .brand-tag { font-size: 8px; font-weight: 600; margin-top: 4px; }
  .headline {
    position: absolute; left: 0; right: 0; top: 148px;
    text-align: center; font-size: 38px; font-weight: 300; letter-spacing: 0.6px;
  }
  .subline {
    position: absolute; left: 0; right: 0; top: 201px;
    text-align: center; font-size: 13px; font-weight: 400; letter-spacing: 1px;
  }
  .signup-panel {
    position: absolute; left: 280px; top: 241px; width: 640px; height: 146px;
    background: var(--panel);
  }
  .field { position: absolute; width: 283px; }
  .field label {
    display: block; font-size: 7.5px; font-weight: 700; letter-spacing: 0.4px;
    height: 9px; margin-bottom: 7px;
  }
  .field .input {
    position: relative; height: 27px; background: var(--field);
    font-size: 10px; color: var(--placeholder); padding: 8px 10px; line-height: 11px;
  }
  .field .input svg { position: absolute; right: 8px; top: 7px; }
  .field-name { left: 20px; top: 21px; }
  .field-company { left: 337px; top: 21px; }
  .field-email { left: 20px; top: 82px; }
  .field-phone { left: 337px; top: 82px; }
  .signup-button {
    position: absolute; left: 538px; top: 405px; width: 124px; height: 39px;
    background: var(--accent); border-bottom: 3px solid var(--accent-dark);
    color: var(--ink-light); font-family: inherit; font-size: 12px; font-weight: 700;
    letter-spacing: 0.5px; text-align: center; line-height: 38px;
  }
  .social-links {
    position: absolute; right: 280px; top: 508px;
    display: flex; gap: 2px; list-style: none;
  }
  .social-links li {
    height: 25px; padding: 0 6px; background: var(--social);
    font-size: 8px; font-weight: 600; line-height: 25px;
  }
  .social-links li:first-child { background: var(--social-dark); }
  .site-footer {
    position: absolute; left: 280px; right: 280px; top: 554px;
    display: flex; justify-content: space-between;
    font-size: 7.5px; font-weight: 400; letter-spacing: 0.2px; color: var(--ink-muted);
  }
  .footer-links { display: flex; gap: 16px; color: var(--ink-light); }
</style>
</head>
<body>
  <div class="hero-backdrop" role="img" aria-label="Photo of a café table with a notebook of sketches, a pen, a smartphone, a tablet on a stand and an iced drink"></div>

  <header class="brand">
    <span class="brand-name">QuenPeak</span>
    <span class="brand-tag">Beta</span>
  </header>

  <h1 class="headline">Social Media Optimization</h1>
  <p class="subline">FOR SMALL TO LARGE BUSINESSES.</p>

  <form class="signup-panel">
    <div class="field field-name">
      <label>FIRST AND LAST NAME *</label>
      <div class="input">Dana Keller
        <svg width="13" height="13" viewBox="0 0 13 13" aria-hidden="true">
          <circle cx="6.5" cy="6.5" r="6.5" fill="var(--ok)"/>
          <path d="M3.6 6.7 L5.7 8.7 L9.5 4.5" fill="none" stroke="#fff" stroke-width="1.6"/>
        </svg>
      </div>
    </div>
    <div class="field field-company">
      <label>COMPANY</label>
      <div class="input"></div>
    </div>
    <div class="field field-email">
      <label>EMAIL *</label>
      <div class="input"></div>
    </div>
    <div class="field field-phone">
      <label>TELEPHONE</label>
      <div class="input"></div>
    </div>
  </form>

  <div class="signup-button">SIGN ME UP</div>

  <ul class="social-links">
    <li>Plinkora</li>
    <li>Wendlo</li>
    <li>Marbix+</li>
  </ul>

  <footer class="site-footer">
    <span>COPYRIGHT © 2014 QUENPEAK. ALL RIGHTS RESERVED.</span>
    <span class="footer-links"><span>Terms of Service</span><span>|</span><span>Privacy Policy</span></span>
  </footer>
</body>
</html>
```